LINGERIE WEBSHOP - Velora casa

We are looking for design and layout design for our webshop. We are company that sells lingerie and other connected textile products liki payamas and etc..
Our website will have approx 500 different products within 2 main catogories Woman/Man) and approx. 10 subcategories
Here is what we expect form design:
-Color pallete should be black and white (if you wish you can add some accent color)
-we want to leave feeling to customers of good quality products towards to luxury
-UX should be simple. Feel free to suggest layout
-frontpage layout, product list layout, product description layout, blog layout
-responsive design, compatible with smartphone

Target Market(s)

woman buying for themself, man buying for woman

Industry/Entity Type

Lingerie

Logo Text

VELORA CASA

Number of Pages Required

4 page

Font styles to use
Sans Serif
Decorative

Requirements
Must have
• simple UX
Nice to have
• difference for sexy/luxury lingerie and daily/cozy lingerie
Should not have
• cheap feel, unreliable

```html
<!DOCTYPE html>
<html lang="en">
<head>
<meta charset="utf-8">
<title>Velora casa – Product List</title>
<link rel="stylesheet" href="https://fonts.googleapis.com/css2?family=Poppins:wght@300;400;500;600&family=Playfair+Display:wght@600&display=swap">
<style>
:root{
  --ink:#222;
  --dark:#3a3a3a;
  --muted:#8a8a8a;
  --soft:#b5b5b5;
  --line:#e2e2e2;
  --panel:#f4f4f4;
  --band:#f3f3f3;
  --white:#fff;
}
*{box-sizing:border-box;margin:0;padding:0}
html,body{width:1200px;height:2895px;overflow:hidden}
body{position:relative;background:var(--white);font-family:'Poppins',sans-serif;color:var(--ink)}

/* header */
.topbar{position:absolute;left:0;top:0;width:1200px;height:71px;background:var(--dark)}
.logo{position:absolute;font-family:'Poppins',sans-serif;font-weight:300;letter-spacing:1px;white-space:nowrap}
.topbar .logo{left:161px;top:30px;font-size:19px;color:var(--white)}
.search{position:absolute;left:458px;top:19px;width:315px;height:33px;border-radius:17px;background:#6a6a6a;color:#ddd;font-size:10px;padding:0 14px;display:flex;align-items:center;justify-content:space-between}
.icons{position:absolute;left:946px;top:26px;display:flex;gap:14px}
.icon{position:relative;width:22px;height:22px}
.badge{position:absolute;right:-6px;top:-6px;font-size:8px;color:var(--white)}

.nav{position:absolute;left:0;top:71px;width:1200px;height:66px;border-bottom:1px solid var(--line);display:flex;justify-content:center;align-items:center;gap:37px;font-size:11.5px;letter-spacing:1px;color:#444}
.nav span{display:inline-flex;align-items:center;gap:4px}
.nav .active{font-weight:600;color:var(--ink);text-decoration:underline;text-underline-offset:4px}

.titleband{position:absolute;left:0;top:137px;width:1200px;height:76px;background:var(--band)}
.titleband h1{position:absolute;left:161px;top:28px;font-size:15px;font-weight:400;letter-spacing:.3px}
.crumbs{position:absolute;right:161px;top:32px;font-size:9.5px;color:var(--soft);letter-spacing:.3px}
.crumbs b{color:var(--ink);font-weight:400}
.crumbs i{font-style:normal;color:#666;margin:0 6px}

/* sidebar */
.side-h{position:absolute;left:161px;font-size:13px;font-weight:500}
.side-h::after{content:"";position:absolute;left:0;top:24px;width:22px;height:1px;background:var(--ink)}
.chk{position:absolute;font-size:10.5px;color:#666;display:flex;align-items:center;gap:9px;white-space:nowrap}
.chk span.box{width:14px;height:14px;border:1px solid #cfcfcf;display:inline-flex;align-items:center;justify-content:center}
.chk.sm span.box{width:11px;height:11px}
.chk.sm{font-size:10px;gap:8px}
.chk.on{color:var(--ink);font-weight:500}
.chev{position:absolute;left:348px;width:8px;height:5px}
.sub{position:absolute;left:205px;font-size:9.5px;color:#888}
.sub.on{color:var(--ink);font-weight:500}
.slider{position:absolute;left:161px;top:742px;width:195px;height:12px}
.slider .track{position:absolute;left:20px;right:20px;top:5px;height:1px;background:var(--line)}
.slider .knob{position:absolute;top:0;width:26px;height:12px;border:1px solid #888;background:var(--white);font-size:6px;text-align:center;line-height:10px;color:#666}
.range{position:absolute;left:160px;top:786px;font-size:10px;color:#666}
.range b{color:var(--ink);font-weight:500}
.btn-filter{position:absolute;left:287px;top:778px;width:69px;height:28px;background:var(--ink);color:var(--white);font-size:10px;font-weight:500;display:flex;align-items:center;justify-content:center}
.swatch{width:14px;height:14px;display:inline-block}

/* toolbar */
.count{position:absolute;left:385px;top:300px;font-size:9px;color:var(--muted);letter-spacing:.2px}
.view{position:absolute;top:289px;width:33px;height:33px;border:1px solid var(--line);display:flex;align-items:center;justify-content:center}
.tlabel{position:absolute;top:300px;font-size:10.5px;font-weight:500}
.select{position:absolute;top:289px;height:33px;border:1px solid var(--line);font-size:9.5px;color:#777;padding:0 10px;display:flex;align-items:center;justify-content:space-between}

/* products */
.grid{position:absolute;left:386px;top:360px;display:grid;grid-template-columns:repeat(3,203px);grid-auto-rows:385px;column-gap:22.5px}
.card{position:relative;text-align:center}
.shot{position:relative;height:255px;background:radial-gradient(ellipse 26% 38% at 50% 48%,#555 0%,#9a9a9a 50%,var(--panel) 100%)}
.heart{position:absolute;right:12px;bottom:-14px;width:29px;height:29px;border-radius:50%;background:#b8b8b8;display:flex;align-items:center;justify-content:center}
.kicker{margin-top:25px;font-size:9.5px;letter-spacing:1.6px;color:var(--soft)}
.name{margin-top:1px;font-size:13px;color:var(--ink)}
.rule{width:22px;height:1px;background:var(--line);margin:9px auto 11px}
.price{font-size:14.5px;font-weight:600}

/* pagination */
.pager{position:absolute;top:1913px;font-size:10px;color:#666;display:flex;align-items:center;gap:6px}
.page{position:absolute;top:1910px;width:26px;height:26px;font-size:10.5px;display:flex;align-items:center;justify-content:center}
.page.cur{background:var(--ink);color:var(--white)}
.divider{position:absolute;left:161px;top:2010px;width:878px;height:1px;background:var(--line)}

/* recommendations */
.rec-title{position:absolute;left:0;top:2078px;width:1200px;text-align:center;font-family:'Playfair Display',serif;font-weight:600;font-size:30px;color:#333}
.rec{position:absolute;left:161px;top:2157px;display:grid;grid-template-columns:repeat(5,158px);column-gap:22px}
.rec .shot{height:209px;background:radial-gradient(ellipse 24% 44% at 50% 52%,#3a3030 0%,#b79a88 45%,#f2f2f2 100%)}
.rec .kicker{margin-top:18px}
.arrow{position:absolute;width:37px;height:37px;display:flex;align-items:center;justify-content:center}
.dots{position:absolute;left:571px;top:2484px;display:flex;gap:10px;align-items:center}
.dot{width:11px;height:11px;border-radius:50%;background:#ddd}
.dot.cur{width:17px;height:17px;border:1px solid #333;background:radial-gradient(circle,#333 45%,transparent 50%)}

/* footer */
.footer{position:absolute;left:0;top:2576px;width:1200px;height:319px;background:var(--band)}
.footer .logo{left:161px;top:75px;font-size:18px;color:var(--ink)}
.fh{position:absolute;top:58px;font-size:13.5px;font-weight:500}
.fl{position:absolute;font-size:10.5px;color:#888}
.fl b{color:var(--ink);font-weight:400}
.news{position:absolute;left:836px;top:112px;width:203px;height:24px;border-bottom:1px solid #cfcfcf;font-size:10.5px;color:#555;display:flex;justify-content:space-between}
.social{position:absolute;left:836px;top:162px;font-size:10px;color:#666;display:flex;gap:11px;align-items:center}
.social i{width:13px;height:13px;border-radius:50%;border:1.5px solid #333;display:inline-block}
.fline{position:absolute;left:161px;top:214px;width:878px;height:1px;background:#e0e0e0}
.copy{position:absolute;left:161px;top:239px;font-size:10.5px}
.cards{position:absolute;right:161px;top:236px;display:flex;gap:6px}
.cards span{width:34px;height:22px;border:1px solid #ccc;background:#e9e9e9}
</style>
</head>
<body>

<svg width="0" height="0" style="position:absolute">
  <symbol id="chev" viewBox="0 0 8 5"><path d="M.5.5L4 4 7.5.5" fill="none" stroke="currentColor" stroke-width="1"/></symbol>
  <symbol id="heart" viewBox="0 0 20 18"><path d="M10 16L2 8.5a4.5 4.5 0 018-5 4.5 4.5 0 018 5z" fill="none" stroke="#fff" stroke-width="2"/></symbol>
</svg>

<header class="topbar">
  <div class="logo">VELORA CASA</div>
  <div class="search">Search Any Product Here
    <svg width="12" height="12" viewBox="0 0 12 12" fill="none" stroke="#ccc"><circle cx="5" cy="5" r="4"/><path d="M8 8l3 3"/></svg>
  </div>
  <div class="icons">
    <div class="icon"><svg width="20" height="20" viewBox="0 0 20 20" fill="#fff"><circle cx="10" cy="6" r="4"/><path d="M2 19c0-5 4-7 8-7s8 2 8 7z"/></svg></div>
    <div class="icon"><svg width="20" height="20" viewBox="0 0 20 20" fill="#fff"><path d="M10 18L2 10a4.5 4.5 0 018-5 4.5 4.5 0 018 5z"/></svg><span class="badge">2</span></div>
    <div class="icon"><svg width="20" height="20" viewBox="0 0 20 20" fill="#fff"><path d="M4 7h12l-1 12H5z"/><path d="M7 7V5a3 3 0 016 0v2" fill="none" stroke="#fff" stroke-width="1.5"/></svg><span class="badge">2</span></div>
  </div>
</header>

<nav class="nav">
  <span>HOME</span><span>ABOUT US</span>
  <span class="active">WOMEN<svg width="7" height="5" style="color:#222"><use href="#chev"/></svg></span>
  <span>MEN<svg width="7" height="5" style="color:#444"><use href="#chev"/></svg></span>
  <span>CHILDREN<svg width="7" height="5" style="color:#444"><use href="#chev"/></svg></span>
  <span>CONTACT US</span>
</nav>

<section class="titleband">
  <h1>PRODUCT LIST</h1>
  <div class="crumbs">HOME<i>›</i>SHOP<i>›</i>WOMEN<i>›</i>LINGERIES<i>›</i><b>LUXURY LINGERIES</b></div>
</section>

<aside>
  <div class="side-h" style="top:289px">Category</div>
  <div class="chk" style="left:161px;top:338px"><span class="box"></span>Male</div><svg class="chev" style="top:343px;color:#999"><use href="#chev"/></svg>
  <div class="chk on" style="left:161px;top:363px"><span class="box"><svg width="10" height="10" viewBox="0 0 10 10"><path d="M1 5l3 3 5-6" fill="none" stroke="#222" stroke-width="1.3"/></svg></span>Female</div><svg class="chev" style="top:369px;color:#222"><use href="#chev"/></svg>
  <div class="chk sm" style="left:185px;top:395px"><span class="box"></span>Underwear</div><svg class="chev" style="top:400px;color:#999"><use href="#chev"/></svg>
  <div class="chk sm" style="left:185px;top:418px"><span class="box"></span>Pijamas</div><svg class="chev" style="top:423px;color:#999"><use href="#chev"/></svg>
  <div class="chk sm" style="left:185px;top:441px"><span class="box"></span>Bikini</div><svg class="chev" style="top:446px;color:#999"><use href="#chev"/></svg>
  <div class="chk sm" style="left:185px;top:463px"><span class="box"></span>T-Shirts</div><svg class="chev" style="top:468px;color:#999"><use href="#chev"/></svg>
  <div class="chk sm" style="left:185px;top:486px"><span class="box"></span>Bra's</div><svg class="chev" style="top:491px;color:#999"><use href="#chev"/></svg>
  <div class="chk sm on" style="left:185px;top:508px"><span class="box"><svg width="8" height="8" viewBox="0 0 10 10"><path d="M1 5l3 3 5-6" fill="none" stroke="#222" stroke-width="1.5"/></svg></span>Lingeries</div><svg class="chev" style="top:514px;color:#222"><use href="#chev"/></svg>
  <div class="sub" style="top:534px">-Casual Lingeries</div>
  <div class="sub on" style="top:558px">-Luxury Lingeries</div>
  <div class="sub" style="top:583px">-Sexy Lingeries</div>
  <div class="chk sm" style="left:185px;top:609px"><span class="box"></span>Panties</div><svg class="chev" style="top:614px;color:#999"><use href="#chev"/></svg>
  <div class="chk sm" style="left:185px;top:631px"><span class="box"></span>Various</div><svg class="chev" style="top:636px;color:#999"><use href="#chev"/></svg>

  <div class="side-h" style="top:691px">Price Filter</div>
  <div class="slider"><div class="track"></div><div class="knob" style="left:0">III</div><div class="knob" style="right:0">III</div></div>
  <div class="range">Price Range : <b>$50 - $100</b></div>
  <div class="btn-filter">FILTER</div>

  <div class="side-h" style="top:855px">Size</div>
  <div class="chk" style="left:161px;top:903px"><span class="box"></span>XS</div>
  <div class="chk" style="left:237px;top:903px"><span class="box"></span>XM</div>
  <div class="chk" style="left:310px;top:903px"><span class="box"></span>XL</div>
  <div class="chk" style="left:161px;top:930px"><span class="box"></span>S</div>
  <div class="chk" style="left:237px;top:930px"><span class="box"></span>L</div>
  <div class="chk" style="left:310px;top:930px"><span class="box"></span>2XL</div>
  <div class="chk" style="left:161px;top:956px"><span class="box"></span>M</div>
  <div class="chk" style="left:237px;top:956px"><span class="box"></span>LS</div>
  <div class="chk" style="left:310px;top:956px"><span class="box"></span>3XL</div>

  <div class="side-h" style="top:1019px">Manufacturer</div>
  <div class="chk" style="left:161px;top:1068px"><span class="box"></span>The Facility Number One</div>
  <div class="chk" style="left:161px;top:1094px"><span class="box"></span>The Facility Number Two</div>
  <div class="chk" style="left:161px;top:1120px"><span class="box"></span>The Facility Number Three</div>

  <div class="side-h" style="top:1184px">Colors</div>
  <div class="chk" style="left:161px;top:1231px"><span class="swatch" style="background:#f6e2c4"></span>Beige</div>
  <div class="chk" style="left:161px;top:1257px"><span class="swatch" style="background:#2a2a2a"></span>Black</div>
  <div class="chk" style="left:161px;top:1284px"><span class="swatch" style="background:#b84a2c"></span>Copper Red</div>
  <div class="chk" style="left:161px;top:1310px"><span class="swatch" style="background:#8c736a"></span>Beige Brown</div>
  <div class="chk" style="left:161px;top:1336px"><span class="swatch" style="background:#eef0e2"></span>Champagne</div>
  <div class="chk" style="left:161px;top:1363px"><span class="swatch" style="background:#8c0b2e"></span>Bordeaux</div>
  <div class="chk" style="left:161px;top:1389px"><span class="swatch" style="background:#b89a80"></span>Bronze Beige</div>
  <div class="chk" style="left:161px;top:1415px"><span class="swatch" style="background:#ee2222"></span>Red</div>

  <div class="side-h" style="top:1480px">Clearance</div>
  <div class="chk" style="left:161px;top:1528px"><span class="box"></span>Up To 30%</div>
  <div class="chk" style="left:161px;top:1554px"><span class="box"></span>Up To 40%</div>
  <div class="chk" style="left:161px;top:1581px"><span class="box"></span>Up To 50%</div>
</aside>

<div class="count">SHOWING 1-12 OF 36 RESULTS</div>
<div class="view" style="left:531px"><svg width="16" height="16" viewBox="0 0 16 16" fill="#333"><rect x="0" y="0" width="7" height="7"/><rect x="9" y="0" width="7" height="7"/><rect x="0" y="9" width="7" height="7"/><rect x="9" y="9" width="7" height="7"/></svg></div>
<div class="view" style="left:572px"><svg width="16" height="14" viewBox="0 0 16 14" fill="#aaa"><rect x="0" y="0" width="3" height="3"/><rect x="5" y="0" width="11" height="3"/><rect x="0" y="5.5" width="3" height="3"/><rect x="5" y="5.5" width="11" height="3"/><rect x="0" y="11" width="3" height="3"/><rect x="5" y="11" width="11" height="3"/></svg></div>
<div class="tlabel" style="left:714px">Filter By:</div>
<div class="select" style="left:765px;width:108px">Category<svg width="8" height="5" style="color:#777"><use href="#chev"/></svg></div>
<div class="tlabel" style="left:884px">Sort By:</div>
<div class="select" style="left:930px;width:109px">Latest<svg width="8" height="5" style="color:#777"><use href="#chev"/></svg></div>

<main class="grid">
  <article class="card"><div class="shot" role="img" aria-label="Photo of black lace lingerie set"><span class="heart"><svg width="13" height="12"><use href="#heart"/></svg></span></div><div class="kicker">LOREM IPSUM</div><div class="name">Lace Pattern Lingeries</div><div class="rule"></div><div class="price">$54.00</div></article>
  <article class="card"><div class="shot" role="img" aria-label="Photo of black lace basque with garters"><span class="heart"><svg width="13" height="12"><use href="#heart"/></svg></span></div><div class="kicker">LOREM IPSUM</div><div class="name">Boneless Underwear Lingerie</div><div class="rule"></div><div class="price">$56.00</div></article>
  <article class="card"><div class="shot" role="img" aria-label="Photo of black satin slip with lace cups"><span class="heart"><svg width="13" height="12"><use href="#heart"/></svg></span></div><div class="kicker">LOREM IPSUM</div><div class="name">Seraphine Lingerie Lace Slip</div><div class="rule"></div><div class="price">$58.00</div></article>

  <article class="card"><div class="shot" role="img" aria-label="Photo of black patterned bodysuit"><span class="heart"><svg width="13" height="12"><use href="#heart"/></svg></span></div><div class="kicker">LOREM IPSUM</div><div class="name">Noctelle Full Cup</div><div class="rule"></div><div class="price">$62.00</div></article>
  <article class="card"><div class="shot" role="img" aria-label="Photo of sheer dotted black bodysuit"><span class="heart"><svg width="13" height="12"><use href="#heart"/></svg></span></div><div class="kicker">LOREM IPSUM</div><div class="name">Children Underwear</div><div class="rule"></div><div class="price">$64.00</div></article>
  <article class="card"><div class="shot" role="img" aria-label="Photo of black lace camisole"><span class="heart"><svg width="13" height="12"><use href="#heart"/></svg></span></div><div class="kicker">LOREM IPSUM</div><div class="name">Lace Camisole</div><div class="rule"></div><div class="price">$66.00</div></article>

  <article class="card"><div class="shot" role="img" aria-label="Photo of black lace bra"><span class="heart"><svg width="13" height="12"><use href="#heart"/></svg></span></div><div class="kicker">LOREM IPSUM</div><div class="name">Ombrelle Luxury Lingerie</div><div class="rule"></div><div class="price">$72.00</div></article>
  <article class="card"><div class="shot" role="img" aria-label="Photo of sheer black babydoll with bows"><span class="heart"><svg width="13" height="12"><use href="#heart"/></svg></span></div><div class="kicker">LOREM IPSUM</div><div class="name">Morning Clavage Lingerie</div><div class="rule"></div><div class="price">$74.00</div></article>
  <article class="card"><div class="shot" role="img" aria-label="Photo of black lace thong"><span class="heart"><svg width="13" height="12"><use href="#heart"/></svg></span></div><div class="kicker">LOREM IPSUM</div><div class="name">Raven Blush Lingerie</div><div class="rule"></div><div class="price">$76.00</div></article>

  <article class="card"><div class="shot" role="img" aria-label="Photo of floral lace bra and briefs"><span class="heart"><svg width="13" height="12"><use href="#heart"/></svg></span></div><div class="kicker">LOREM IPSUM</div><div class="name">Floral Lace Lingeries</div><div class="rule"></div><div class="price">$82.00</div></article>
  <article class="card"><div class="shot" role="img" aria-label="Photo of black satin nightdress"><span class="heart"><svg width="13" height="12"><use href="#heart"/></svg></span></div><div class="kicker">LOREM IPSUM</div><div class="name">Nightwear Clavage Lingerie</div><div class="rule"></div><div class="price">$84.00</div></article>
  <article class="card"><div class="shot" role="img" aria-label="Photo of black strappy bra and briefs"><span class="heart"><svg width="13" height="12"><use href="#heart"/></svg></span></div><div class="kicker">LOREM IPSUM</div><div class="name">Royal Blush Lingerie</div><div class="rule"></div><div class="price">$86.00</div></article>
</main>

<div class="pager" style="left:385px"><svg width="12" height="10" viewBox="0 0 12 10" fill="none" stroke="#666"><path d="M11 5H1M5 1L1 5l4 4"/></svg>PREV</div>
<div class="page" style="left:668px">1</div>
<div class="page cur" style="left:698px">2</div>
<div class="page" style="left:730px">3</div>
<div class="pager" style="left:996px;color:#222">NEXT<svg width="12" height="10" viewBox="0 0 12 10" fill="none" stroke="#222"><path d="M1 5h10M7 1l4 4-4 4"/></svg></div>
<div class="divider"></div>

<h2 class="rec-title">Top Recommendations</h2>
<section class="rec">
  <article class="card"><div class="shot" role="img" aria-label="Model wearing a sheer black babydoll"></div><div class="kicker">LOREM IPSUM</div><div class="name">Lingerie Babydoll</div><div class="rule"></div><div class="price">$23.00</div></article>
  <article class="card"><div class="shot" role="img" aria-label="Model wearing a fishnet bodysuit"></div><div class="kicker">LOREM IPSUM</div><div class="name">Fishnet Lingeries</div><div class="rule"></div><div class="price">$39.00</div></article>
  <article class="card"><div class="shot" role="img" aria-label="Model wearing a black bra and panties set"></div><div class="kicker">LOREM IPSUM</div><div class="name">Bra and Panties</div><div class="rule"></div><div class="price">$16.00</div></article>
  <article class="card"><div class="shot" role="img" aria-label="Model wearing a black satin sleep dress"></div><div class="kicker">LOREM IPSUM</div><div class="name">Sleeping Lingerie</div><div class="rule"></div><div class="price">$57.00</div></article>
  <article class="card"><div class="shot" role="img" aria-label="Model wearing a sheer zip-front bodysuit"></div><div class="kicker">LOREM IPSUM</div><div class="name">Midnight Lingerie Set</div><div class="rule"></div><div class="price">$46.00</div></article>
</section>
<div class="arrow" style="left:143px;top:2244px;background:#e4e4e4"><svg width="16" height="12" viewBox="0 0 16 12" fill="none" stroke="#555"><path d="M15 6H1M6 1L1 6l5 5"/></svg></div>
<div class="arrow" style="left:1016px;top:2266px;background:#333"><svg width="16" height="12" viewBox="0 0 16 12" fill="none" stroke="#fff"><path d="M1 6h14M10 1l5 5-5 5"/></svg></div>
<div class="dots"><span class="dot"></span><span class="dot cur"></span><span class="dot"></span></div>

<footer class="footer">
  <div class="logo">VELORA CASA</div>
  <div class="fl" style="left:161px;top:112px"><b>Phone Number:</b> 01/5280-316</div>
  <div class="fl" style="left:161px;top:138px"><b>E-Mail Address:</b> info@veloracasa.hr</div>
  <div class="fl" style="left:161px;top:165px"><b>Working Hours:</b> Mon – Sat: 09 – 21 h</div>

  <div class="fh" style="left:388px">Find Us At</div>
  <div class="fl" style="left:388px;top:112px">Terms Of Use</div>
  <div class="fl" style="left:388px;top:138px">Terms Of Purchase</div>
  <div class="fl" style="left:388px;top:165px">Privacy Policy</div>

  <div class="fh" style="left:612px">Information</div>
  <div class="fl" style="left:612px;top:112px">Payment Methods</div>
  <div class="fl" style="left:612px;top:138px">Delivery &amp; Shipping</div>
  <div class="fl" style="left:612px;top:165px">Returns &amp; Refunds</div>

  <div class="fh" style="left:836px">Newsletter</div>
  <div class="news"><span>Your E-mail Address</span><svg width="12" height="12" viewBox="0 0 12 12" fill="none" stroke="#444"><path d="M1 6l10-5-3 10-2-4z"/></svg></div>
  <div class="social">Find Us At: <i aria-label="Social link"></i><i aria-label="Social link"></i><i aria-label="Social link"></i><i aria-label="Social link"></i><i aria-label="Social link"></i></div>

  <div class="fline"></div>
  <div class="copy"><b style="font-weight:500">Copyright © 2020 Velora casa.</b> <span style="color:#666">All Rights Reserved</span></div>
  <div class="cards"><span aria-label="Payment card"></span><span aria-label="Payment card"></span><span aria-label="Payment card"></span></div>
</footer>

</body>
</html>
```